North Fern Holdings Business Card

A business card design to accompany the logo design you completed on Artisan Hive. We are open to your proposals. I did add one idea below that might work, but we aren't married to the idea. The company is a real estate services company. Clientele are typically high net worth individuals, executive level employment or owners of their own company, 30-60 years old.

Our 1 (bad?) idea: double sided card; One side landscape with logo and word mark. Other side Portrait with the logo only (oversize watermark maybe?). Somewhere add text of Name (Marcus Pellington), Title (Principal), phone # (949-555-0173) and email address (marcus@northfernhq.com). There would be a second design with my wife's name, number and email in place of mine.

Again totally open to ideas here.

Industry/Entity Type

Real Estate

```html
<!DOCTYPE html>
<html lang="en">
<head>
<meta charset="utf-8">
<title>North Fern Holdings Business Card</title>
<link rel="stylesheet" href="https://fonts.googleapis.com/css2?family=Cinzel:wght@400&family=Marcellus+SC&family=Arimo:ital@0;1&display=swap">
<style>
  :root {
    --page: #ece9e4;
    --paper: #ffffff;
    --sage: #659a5a;
    --sage-mid: #86ae7b;
    --sage-pale: #a9c49f;
    --ink-light: #ffffff;
    --card-shadow: rgba(0, 0, 0, 0.18);
  }
  * { margin: 0; padding: 0; box-sizing: border-box; }
  html, body {
    width: 900px;
    height: 1200px;
    overflow: hidden;
    background: var(--page);
  }
  .sheet {
    position: relative;
    width: 900px;
    height: 1200px;
  }
  .card {
    position: absolute;
    left: 170px;
    width: 560px;
    height: 320px;
    box-shadow: 0 6px 18px var(--card-shadow);
    overflow: hidden;
  }
  .card--front {
    top: 220px;
    background: var(--paper);
  }
  .brand-square {
    position: absolute;
    left: 225px;
    top: 58px;
    width: 110px;
    height: 110px;
    background: var(--sage);
  }
  .brand-name {
    position: absolute;
    left: 0;
    right: 0;
    top: 200px;
    text-align: center;
    font-family: "Cinzel", serif;
    font-weight: 400;
    font-size: 30px;
    line-height: 40px;
    color: var(--sage);
    letter-spacing: 0.02em;
  }
  .card--back {
    top: 660px;
    background: var(--sage);
  }
  .watermark-area {
    position: absolute;
    left: 0;
    top: 0;
    width: 380px;
    height: 320px;
    background:
      radial-gradient(ellipse 300px 340px at 120px 140px,
        var(--sage-pale) 0%,
        var(--sage-pale) 35%,
        var(--sage-mid) 70%,
        var(--sage) 100%);
  }
  .contact {
    position: absolute;
    left: 326px;
    top: 212px;
    color: var(--ink-light);
  }
  .contact__name {
    font-family: "Marcellus SC", serif;
    font-size: 20px;
    letter-spacing: 0.03em;
    margin-bottom: 8px;
  }
  .contact__title,
  .contact__line {
    font-family: "Arimo", sans-serif;
    font-size: 13px;
    line-height: 16px;
  }
  .contact__title { font-style: italic; }
</style>
</head>
<body>
  <main class="sheet">
    <section class="card card--front" aria-label="Card front">
      <div class="brand-square"></div>
      <div class="brand-name">North Fern Holdings</div>
    </section>

    <section class="card card--back" aria-label="Card back">
      <div class="watermark-area" role="img" aria-label="Oversized pale company emblem watermark bleeding off the left edge"></div>
      <div class="contact">
        <p class="contact__name">Marcus Pellington</p>
        <p class="contact__title">Principal</p>
        <p class="contact__line">949-555-0173</p>
        <p class="contact__line">marcus@northfernhq.com</p>
      </div>
    </section>
  </main>
</body>
</html>
```